Values Statement poster template

We want to develop a poster template for our company policies and statements which promote our company values in our workplaces.
These documents are important in showing our clients, suppliers and employees who we are and what we stand for.
The graphic design will incorporate our company logo, and be bright, uplifting and inspiring, developing a graphic theme that we can utilise for other company documents. The design will graphically illustrate and support our values statement, with colour and modern design.
This values poster will be the first in a series of documents using the same theme.The format will be a4 and a3 portrait
We are an environmental service business specialising in rehabilitation and revegetation

Target Market(s)

Tier one clients in industry, Mining, Construction and agriculture

Font styles to use
Other font styles liked:
• calibri

Requirements
Must have
• Professional , high end feel, able to read clearly on a poster
Nice to have
• graphic design elements, symbols, etc which support the message, that can be carried through to various documents such as quality, environmental, safety policies
A bright theme which ties in with our logo colours.

```html
<!DOCTYPE html>
<html lang="en">
<head>
<meta charset="utf-8">
<title>Values Statement Poster</title>
<link href="https://fonts.googleapis.com/css2?family=Carlito:wght@400;700&display=swap" rel="stylesheet">
<style>
  :root {
    --canvas-bg: #e6e8eb;
    --paper: #ffffff;
    --navy: #1f2a8a;
    --ink: #2a2a2a;
    --brand-green: #17703a;
    --band-green: #3fae3a;
    --title: #ffffff;
    --corner-navy: #232c7e;
  }
  * { box-sizing: border-box; margin: 0; padding: 0; }
  html, body { width: 1200px; height: 902px; overflow: hidden; }
  body { background: var(--canvas-bg); font-family: "Carlito", "Calibri", sans-serif; color: var(--ink); }

  .poster {
    position: absolute; left: 296px; top: 21px;
    width: 608px; height: 860px;
    background: var(--paper);
    box-shadow: 0 4px 18px rgba(0,0,0,.18);
    overflow: hidden;
  }
  .poster-art { position: absolute; inset: 0; width: 608px; height: 860px; }

  .values-title {
    position: absolute; left: 200px; top: 82px;
    font-size: 96px; font-weight: 700; line-height: 1;
    color: var(--title);
  }

  .brand {
    position: absolute; left: 292px; top: 296px;
    display: flex; align-items: center; gap: 10px;
  }
  .brand-dot { width: 24px; height: 24px; border-radius: 50%; background: var(--brand-green); }
  .brand-name { font-size: 35px; font-weight: 700; color: var(--brand-green); line-height: 1; }

  .column { position: absolute; top: 0; }
  .column-left { left: 53px; width: 218px; }
  .column-right { left: 314px; width: 250px; }

  .value { position: absolute; left: 0; width: 100%; }
  .value h2 { font-size: 22px; font-weight: 700; color: var(--navy); line-height: 1; }
  .value .tagline {
    display: block; text-align: right;
    font-size: 10px; font-weight: 700; color: var(--navy); line-height: 1.1;
  }
  .value p, .value li { font-size: 8.6px; line-height: 11px; }
  .value p { margin-top: 3px; }
  .value ul { list-style: none; margin-top: 2px; }
  .value li { padding-left: 7px; text-indent: -6px; }
  .value li::before { content: "• "; }
</style>
</head>
<body>
  <main class="poster">
    <svg class="poster-art" viewBox="0 0 608 860">
      <defs>
        <linearGradient id="landscape" x1="0" y1="0" x2="0" y2="1">
          <stop offset="0" stop-color="#e9d7b4"/>
          <stop offset=".12" stop-color="#b9a46a"/>
          <stop offset=".35" stop-color="#6f8a3c"/>
          <stop offset=".7" stop-color="#2f5a22"/>
          <stop offset="1" stop-color="#1f4318"/>
        </linearGradient>
        <radialGradient id="continent" cx=".5" cy=".5" r=".5">
          <stop offset="0" stop-color="#e6e7ea"/>
          <stop offset="1" stop-color="#ffffff" stop-opacity="0"/>
        </radialGradient>
      </defs>

      <rect class="landscape-photo" x="0" y="0" width="608" height="860" fill="url(#landscape)"
            role="img" aria-label="Aerial photograph of green forested hills and a winding highway at sunrise"/>

      <path class="band" d="M0,345 Q280,270 560,212 L563,215 Q300,300 0,405 Z" fill="var(--band-green)"/>

      <path class="page" d="M0,405 Q300,300 563,215 L606,680 L470,860 L0,860 Z" fill="var(--paper)"/>

      <ellipse class="continent-watermark" cx="300" cy="560" rx="270" ry="230" fill="url(#continent)"
               role="img" aria-label="Faint map of the continent behind the values text"/>

      <path class="corner" d="M606,680 L608,680 L608,860 L470,860 Z" fill="var(--corner-navy)"
            role="img" aria-label="National flag in the lower corner"/>
    </svg>

    <div class="values-title">Values</div>

    <div class="brand">
      <span class="brand-dot"></span>
      <span class="brand-name">Greenhollow</span>
    </div>

    <section class="column column-left">
      <article class="value" style="top:396px">
        <h2>We value our people</h2>
        <span class="tagline">above everything else</span>
        <p>We demonstrate this by:</p>
        <ul>
          <li>Providing safe, positive, enjoyable workplaces where everyone feels valued and respected</li>
          <li>Providing Careers, not Jobs, we grow together</li>
          <li>Encouraging inclusion, participation and collaboration</li>
          <li>Recognising and rewarding contribution and excellence</li>
          <li>Supporting our people through tough times</li>
        </ul>
      </article>
      <article class="value" style="top:524px">
        <h2>We do good things</h2>
        <span class="tagline">for the planet</span>
        <p>Our products are helping revegetate Australia,<br>which we are tremendously proud of.<br>We minimise our environmental impact in<br>everything we do.</p>
      </article>
      <article class="value" style="top:612px">
        <h2>We set the standard</h2>
        <ul>
          <li>We are uncompromising on quality</li>
          <li>We are the best at what we do, and we do what we are best at</li>
          <li>We are always improving</li>
          <li>We are pioneering</li>
        </ul>
      </article>
      <article class="value" style="top:700px">
        <h2>We are proud<br>of who we are</h2>
        <p>Our reputation means the world to us. We:</p>
        <ul>
          <li>Treat everyone with respect and we expect it in return</li>
          <li>Follow the rules</li>
          <li>Do what we say we will do</li>
          <li>Own our mistakes and we fix them</li>
          <li>Are trustworthy and transparent</li>
        </ul>
      </article>
    </section>

    <section class="column column-right">
      <article class="value" style="top:396px">
        <h2>Our workplaces are safe</h2>
        <p>There is nothing more important to us than our people going home healthy and safe every day. We won’t accept anything less. We believe safety is a management choice. By providing safe work systems, and education we achieve our daily goal of Zero Harm. At Greenhollow we;</p>
        <ul>
          <li>Take the time to make our work areas safe, whatever it takes</li>
          <li>Don’t accept shortcuts</li>
          <li>Look out for each other</li>
          <li>Investigate our incidents and learn from them, we won’t accept repeats</li>
          <li>Are constantly looking for ways to improve the safety of our workplaces.</li>
          <li>Think safe, work safer, go home safe!</li>
        </ul>
      </article>
      <article class="value" style="top:580px">
        <h2>We succeed together</h2>
        <p>We believe in win-win relationships. When our business is profitable everyone benefits, our owners, employees, clients and the community. At Greenhollow we:</p>
        <ul>
          <li>Work as a team, we get it done together</li>
          <li>We treat our suppliers and subcontractors like they are part of the team.</li>
          <li>Are building on our success, and growing together</li>
          <li>Choose to work with employees, customers and suppliers who fit our values</li>
        </ul>
      </article>
      <article class="value" style="top:718px; width:160px">
        <h2>We give back</h2>
        <p>We appreciate our success and we give back by supporting our community, and those less fortunate.</p>
      </article>
    </section>
  </main>
</body>
</html>
```